AI Layout work for Business Cards, Letterhead and Compliment Slip for Award-winning UK Property Deve

No actual logo or corporate identity design work needed here but some skill required to create layouts for business card, letterhead and compliment slip for this award-winning company.
I can provide AI files featuring the company logo and an initial layout of the business card, (6 versions featuring the same design but for different personnel), along with some initial instructions (with possibly more to follow from the client). The finished layouts for each item need to be print-ready in AI format - 8 in all (6 for each business card plus 1 for letterhead and 1 for compliment slip).
I've given this project a 5-day duration but there may be some flexibility built into that depending on client feedback. Hopefully that won't be a problem.
UPDATE:
The client has been very prescriptive about the layout and design of these. To that end, please find 3 additional pdfs that explain what's required.
1.
All BUSINESS CARDS need to be laid out as per the attached AI file (but see latest pdf to check which layout - there are 2 in the original AI file). Use the details in the VEL-contact-details.pdf to create 6 individual AI files, one for each card.
2.
Create 2 additional AI files, one each for the LETTERHEAD and the COMPLIMENT SLIP based on the latest mock-up that I've provided (letterhead-layout-final.pdf)
In all, I need EIGHT individual AI files, 6 for each business card, 1 for the letterhead and 1 for the compliment slip. I'd like to get this done as soon as possible now please.
Target Market(s)
Purchasers of upmarket luxury properties - see here: http://www.velproperties.co.uk
Industry/Entity Type
Business
Requirements
Must have
- Layouts need to be cool, understated and uncluttered.
Nice to have
- Please keep it simple! The actual logo background colour is likely to change (awaiting confirmation from client) but accompanying text detail and font (Deja Vu Sans Condensed) can remain as seen in the files below - for the time being at least! That having been said, I'm open to suggestions.
Should not have
- Nothing extreme or ostentatious please.

```html
<!DOCTYPE html>
<html lang="en">
<head>
<meta charset="utf-8">
<title>VEL Business Card</title>
<link href="https://fonts.googleapis.com/css2?family=Encode+Sans+Condensed:wght@400;500&display=swap" rel="stylesheet">
<style>
  :root {
    --bg: #ececec;
    --navy: #171c47;
    --charcoal: #444546;
    --white: #ffffff;
    --soft: #d9dbe6;
    --rule: #8a8468;
  }
  * { margin: 0; padding: 0; box-sizing: border-box; }
  html, body { width: 1200px; height: 1000px; overflow: hidden; }
  body {
    background: var(--bg);
    font-family: "Encode Sans Condensed", "DejaVu Sans Condensed", sans-serif;
    display: flex;
    align-items: center;
    justify-content: center;
    gap: 60px;
  }
  .card {
    position: relative;
    width: 510px;
    height: 330px;
    background: var(--navy);
    overflow: hidden;
    box-shadow: 0 6px 18px rgba(0,0,0,0.18);
  }
  .card-front .split { position: absolute; inset: 0; }
  .brand-name {
    position: absolute;
    left: 50%;
    top: 50%;
    transform: translate(-50%, -50%);
    color: var(--white);
    font-weight: 400;
    font-size: 74px;
    letter-spacing: 4px;
    line-height: 1;
  }
  .card-back { color: var(--soft); }
  .person {
    position: absolute;
    left: 38px;
    top: 40px;
  }
  .person-name {
    font-size: 19px;
    font-weight: 500;
    letter-spacing: 2px;
    color: var(--white);
  }
  .person-role {
    font-size: 17px;
    letter-spacing: 1px;
    margin-top: 4px;
    color: var(--white);
  }
  .divider {
    position: absolute;
    left: 38px;
    right: 38px;
    top: 112px;
    height: 1px;
    background: var(--rule);
  }
  .contact {
    position: absolute;
    left: 38px;
    top: 132px;
    list-style: none;
    font-size: 13.5px;
    line-height: 1.55;
  }
  .address {
    position: absolute;
    left: 38px;
    bottom: 30px;
    list-style: none;
    font-size: 13.5px;
    line-height: 1.55;
  }
  .address li::before { content: "\2022\00a0"; }
  .brand-mark {
    position: absolute;
    right: 38px;
    bottom: 38px;
    color: var(--white);
    font-size: 34px;
    letter-spacing: 2px;
    line-height: 1;
  }
</style>
</head>
<body>
  <section class="card card-front">
    <svg class="split" width="510" height="330" viewBox="0 0 510 330" aria-hidden="true">
      <polygon points="0,0 510,0 510,110 0,250" fill="var(--charcoal)"/>
    </svg>
    <div class="brand-name">VEL</div>
  </section>

  <section class="card card-back">
    <div class="person">
      <div class="person-name">THOMAS HALE</div>
      <div class="person-role">Director</div>
    </div>
    <div class="divider"></div>
    <ul class="contact">
      <li>T: +44 (0)1632 960418</li>
      <li>E: enquiries@velproperties.co.uk</li>
      <li>W: velproperties.co.uk</li>
    </ul>
    <ul class="address">
      <li>VEL Exclusive Properties</li>
      <li>Ashcombe House &bull; Ashcombe Lane</li>
      <li>Little Brampton &bull; ZZ9 4QX</li>
    </ul>
    <div class="brand-mark">VEL</div>
  </section>
</body>
</html>
```